Corvana Wound Care Business card design

We need a business card designed around our logo which was provided. The logo of preference is the colored. Also the colors and fonts were provided.

Target Market(s)

Our Referral partners are home health agencies.

Industry/Entity Type

Healthcare

Contact Information for Business Card

Name , Phone #, Email , Title

Requirements
Nice to have
• Creativity
Should not have
• basic

```html
<!DOCTYPE html>
<html lang="en">
<head>
<meta charset="UTF-8">
<title>Corvana Wound Care – Business Card</title>
<link href="https://fonts.googleapis.com/css2?family=Lato:wght@400;700;900&display=swap" rel="stylesheet">
<style>
  :root{
    --page:#f2f2f2;
    --card-dark:#111214;
    --card-dark-2:#1c1d20;
    --card-light:#ffffff;
    --brand-blue:#1f4fb8;
    --brand-navy:#1c2f7a;
    --brand-sky:#3b8fe0;
    --text-light:#ffffff;
    --text-soft:#e6e6e6;
    --faint:#ececec;
  }
  *{box-sizing:border-box;margin:0;padding:0}
  html,body{width:1200px;height:900px;overflow:hidden}
  body{background:var(--page);font-family:"Lato",sans-serif;position:relative}

  .card{position:absolute;top:300px;width:520px;height:300px;border-radius:24px;overflow:hidden;
        box-shadow:0 10px 24px rgba(0,0,0,.18)}

  /* Front */
  .card--front{left:50px;background:linear-gradient(160deg,var(--card-dark-2),var(--card-dark) 60%)}
  .card--front .backdrop{position:absolute;left:0;top:0;width:200px;height:220px;
        background:radial-gradient(circle at 30% 40%,rgba(255,255,255,.06),transparent 70%)}
  .card--front .brand{position:absolute;left:100px;top:112px;display:flex;align-items:center;gap:14px}
  .brand-mark{width:26px;height:26px;border-radius:50%;background:var(--brand-blue)}
  .brand-name{font-weight:700;font-size:40px;color:var(--brand-blue);letter-spacing:.5px;line-height:1}
  .brand-sub{font-weight:700;font-size:40px;color:var(--brand-blue)}
  .card--front .website{position:absolute;left:0;right:0;top:218px;text-align:center;
        color:var(--text-light);font-weight:700;font-size:19px;letter-spacing:.3px}

  /* Back */
  .card--back{left:630px;background:var(--card-dark)}
  .back-top{position:absolute;left:0;top:0;width:100%;height:162px;background:var(--card-light)}
  .back-top .backdrop{position:absolute;inset:0;
        background:linear-gradient(90deg,var(--faint),var(--card-light) 35%,var(--card-light) 65%,var(--faint))}
  .back-top .brand{position:absolute;left:0;right:0;top:58px;display:flex;justify-content:center;align-items:center;gap:12px}
  .back-top .brand-name{font-size:34px;color:var(--brand-navy)}
  .back-top .brand-mark{width:22px;height:22px;background:var(--brand-navy)}
  .divider{position:absolute;left:0;top:162px;width:100%;height:7px;
        background:linear-gradient(90deg,var(--brand-navy),var(--brand-sky) 50%,var(--brand-navy))}
  .back-bottom{position:absolute;left:0;top:169px;width:100%;height:131px;
        background:linear-gradient(170deg,var(--card-dark-2),var(--card-dark))}
  .person{position:absolute;left:34px;top:22px;color:var(--text-light)}
  .person-name{font-weight:900;font-size:21px;letter-spacing:.5px;text-transform:uppercase}
  .person-title{font-weight:700;font-size:11.5px;margin-top:6px;color:var(--text-soft)}
  .icon-rail{position:absolute;left:262px;top:12px;width:26px;height:108px;border-radius:13px;
        background:var(--brand-blue);display:flex;flex-direction:column;justify-content:space-around;align-items:center}
  .icon-rail svg{width:14px;height:14px;fill:var(--text-light)}
  .contacts{position:absolute;left:300px;top:12px;color:var(--text-light);font-size:14.5px;font-weight:700;line-height:1.25}
  .contacts li{list-style:none}
  .contacts .phone{margin-bottom:10px}
  .contacts .address{margin-bottom:10px}
</style>
</head>
<body>

<section class="card card--front" aria-label="Business card front">
  <div class="backdrop" role="img" aria-label="Faint decorative shapes"></div>
  <div class="brand">
    <span class="brand-mark"></span>
    <span class="brand-name">Corvana Wound Care</span>
  </div>
  <p class="website">www.corvanacare.com</p>
</section>

<section class="card card--back" aria-label="Business card back">
  <div class="back-top">
    <div class="backdrop" role="img" aria-label="Faint decorative pattern"></div>
    <div class="brand">
      <span class="brand-mark"></span>
      <span class="brand-name">Corvana Wound Care</span>
    </div>
  </div>
  <div class="divider"></div>
  <div class="back-bottom">
    <div class="person">
      <p class="person-name">Dana Whitfield</p>
      <p class="person-title">Certified Wound Care Specialist</p>
    </div>
    <div class="icon-rail">
      <svg viewBox="0 0 24 24" aria-label="Phone"><path d="M6.6 10.8a15.5 15.5 0 0 0 6.6 6.6l2.2-2.2c.3-.3.7-.4 1-.2 1.1.4 2.3.6 3.6.6.6 0 1 .4 1 1V20c0 .6-.4 1-1 1A17 17 0 0 1 3 4c0-.6.4-1 1-1h3.5c.6 0 1 .4 1 1 0 1.3.2 2.5.6 3.6.1.3 0 .7-.2 1z"/></svg>
      <svg viewBox="0 0 24 24" aria-label="Location"><path d="M12 2a7 7 0 0 0-7 7c0 5.3 7 13 7 13s7-7.7 7-13a7 7 0 0 0-7-7zm0 9.5A2.5 2.5 0 1 1 12 6.5a2.5 2.5 0 0 1 0 5z"/></svg>
      <svg viewBox="0 0 24 24" aria-label="Email"><path d="M3 5h18v14H3z" opacity=".0"/><path d="M3 5h18v2l-9 6-9-6zM3 9l9 6 9-6v10H3z"/></svg>
    </div>
    <ul class="contacts">
      <li class="phone">+1 (214) 555-0194</li>
      <li class="address">1180 Harbor Clinic Way,<br>Dallas, TX 75204</li>
      <li class="email">care@corvanacare.com</li>
    </ul>
  </div>
</section>

</body>
</html>
```